Flyer Design Project for The Amberfield Company

I'm a Naturopathic Herbalist who wishes to expand my business from x1 a week to x5 days a week and so need to produce a flyer to let people know what I do and to guide them to my website at theamberfieldcompany.com.au.
One-sided or double-sided A5 flyer on good quality paper for distribution by my referral network.  If all the info can fit on one side that would be great.
It would be great if the design could link up with my website i.e. the sun, mountains etc in the background but don't worry if not possible so then as an alternative I'd like to see something modern, fresh.
Otherwise it's to be simple, clean, easy to read, with a couple of relevant pictures if you want.

Target Market(s)
Predominantly females, from teens "clear skin tonics" to overloaded twenty-somethings, to pre-baby fertility programmes, healthy pregnancy etc
Industry/Entity Type
Business
Look and feel

```html
<!DOCTYPE html>
<html lang="en">
<head>
<meta charset="utf-8">
<title>The Amberfield Company – Herbal Medicine Flyer</title>
<link rel="stylesheet" href="https://fonts.googleapis.com/css2?family=Arimo:wght@400;700&family=Oswald:wght@300&family=Raleway:wght@300&display=swap">
<style>
  :root {
    --plum: #a4508c;
    --plum-deep: #8a3f78;
    --plum-mist: #c48ab4;
    --leaf: #00a859;
    --white: #ffffff;
    --shadow: rgba(0,0,0,0.25);
  }
  * { margin: 0; padding: 0; box-sizing: border-box; }
  html, body { width: 1200px; height: 852px; overflow: hidden; background: var(--white); }
  .flyer { position: relative; width: 1200px; height: 852px; display: flex; }

  .cover {
    position: relative; width: 599px; height: 852px;
    background: var(--plum); color: var(--white); overflow: hidden;
    border-right: 1px solid #d9d9d9;
  }
  .cover__scene {
    position: absolute; left: 0; top: 420px; width: 100%; height: 432px;
    background: linear-gradient(180deg, var(--plum) 0%, #a65a92 20%, var(--plum-mist) 45%, #9a4f86 70%, var(--plum-deep) 100%);
  }
  .cover__headline {
    position: absolute; top: 112px; left: 0; width: 100%;
    font-family: "Oswald", sans-serif; font-weight: 300;
    font-size: 49px; line-height: 59px; text-align: center; letter-spacing: -0.3px;
  }
  .cover__tagline {
    position: absolute; top: 386px; left: 0; width: 100%;
    font-family: "Raleway", sans-serif; font-weight: 300;
    font-size: 35px; line-height: 34px; text-align: center; text-transform: uppercase;
  }

  .info {
    position: relative; width: 601px; height: 852px; background: var(--leaf); color: var(--white);
    font-family: "Arimo", sans-serif; font-size: 11.8px; line-height: 23.2px;
  }
  .info__plant {
    float: left; width: 60px; height: 64px; margin: 0 12px 0 0;
    background: radial-gradient(circle at 50% 40%, #7fb85a, #3f7a2e 60%, #e9efe4 61%);
    border: 2px solid var(--white);
  }
  .info__column { position: absolute; top: 56px; width: 232px; text-align: justify; }
  .info__column--first { left: 54px; }
  .info__column--second { left: 318px; }
  .info__column p { margin-bottom: 23px; }
  .info__column p.tight { margin-bottom: 0; }
  .info__column p.compact { line-height: 15px; }
  .info__column .web { font-weight: 700; letter-spacing: 0; }

  .contact { position: absolute; left: 113px; top: 652px; width: 380px; height: 145px; }
  .contact svg { position: absolute; inset: 0; }
  .contact__text {
    position: absolute; top: 36px; left: 0; width: 100%; text-align: center;
    color: #222; font-family: "Arimo", sans-serif; font-size: 13px; line-height: 15.5px;
  }
  .contact__name { color: var(--leaf); font-weight: 700; font-size: 15.5px; line-height: 19px; }
</style>
</head>
<body>
<div class="flyer">
  <section class="cover">
    <div class="cover__scene" role="img" aria-label="Photograph of a snow-capped mountain above a pine forest, tinted purple"></div>
    <h1 class="cover__headline">Are you feeling tired, run down,<br>under the weather or simply just<br>feeling out of balance?</h1>
    <p class="cover__tagline">Herbal medicine could<br>be the answer for you.</p>
  </section>

  <section class="info">
    <div class="info__column info__column--first">
      <p><span class="info__plant" role="img" aria-label="Photograph of a potted herb plant"></span>Maren has a wealth of experience with over 14 years in clinical practice which, coupled with a great deal of “life experience” as the mother of three children, helps to make your consultation professional, caring and healing.</p>
      <p>Passionate about helping you reach your highest potential health-wise, Maren will make you a “Daily Wellness Tonic” which is like the best multi-vitamin you could have as it's tailor-made especially for you. The “Daily Wellness Tonic” can help strengthen, nourish, heal and rebalance your whole body.</p>
      <p class="tight">“Daily Wellness Tonics” can be made to assist you keeping yourself well, for nurturing yourself (so in turn you can nurture others), for re-energising you, for aging gracefully, to assist you feeling</p>
    </div>
    <div class="info__column info__column--second">
      <p>back on top of life and to help you face challenges more easily.<br>Herbal medicine can help with Sleep Disorders, Weak Immune Systems, Anxiety, Depression, Fertility issues, Childhood Diseases, Skin Problems, Gastro-Intestinal Disorders and Women's Health.</p>
      <p>Maren also specialises in “Super Immune Boost Tonics” assisting with acute conditions such as coughs, colds, sore throats and offers 20-30 minute “Express Appointments”. Useful as a preventative measure or as a way of healing these conditions more quickly.</p>
      <p class="compact">&nbsp;“Clear Skin Wellness Tonics” are popular with teens and a special teen package is also offered as an “Express Appointment” with a bottle of tonic.</p>
      <p class="compact" style="margin-top:28px">For more information, check out The Amberfield Company website at <span class="web">www.theamberfieldcompany.com.au</span></p>
    </div>

    <div class="contact">
      <svg width="380" height="145" viewBox="0 0 380 145" aria-hidden="true">
        <path d="M97 4 H185 V24 H366 V115 H248 V143 H97 V115 H0 V24 H97 Z" fill="var(--shadow)" transform="translate(3,3)"/>
        <path d="M97 4 H185 V24 H366 V115 H248 V143 H97 V115 H0 V24 H97 Z" fill="var(--white)"/>
      </svg>
      <div class="contact__text" style="width:366px">
        <div class="contact__name">Maren Holt DHM,</div>
        <div>Local Naturopathic Herbalist</div>
        <div>joins the professional team at Willowbrook Natural Health</div>
        <div>48 Harlow Street, Fernvale, NSW, 2099</div>
        <div>Ph: 0400 555 018</div>
      </div>
    </div>
  </section>
</div>
</body>
</html>
```